Harrowgate Recruitment Flyer "Your Career Starts Here"

Objective of this project is to design a flyer for our company's recruitment efforts on college campuses while looking for students to hire for our software engineer and trading summer internships. Our target audience are students who are juniors in college (19-22 years old) that are mostly computer science majors.
I would like the design to be on one page, front and back (we will be printing these professionally on glossy paper).
We are looking to change the "feel" of our literature:
On the front side of the flyer I want to include:
1. The graphics/icons and benefits that we have on our new banners (you will see this in file 3). There is a list of 6 things on the banners, if you could list those and leave room for me to expand on each point, that would be great.
2. Background about Harrowgate's history:
Harrowgate is a diversified financial institution specializing in proprietary trading, asset management, order execution services, and technology solutions. We are recognized as a market leader in derivatives valuation, trading, and value-added order execution across global equity, options, and futures markets. Our focus on innovation, achievement, and integrity serves the interests of our clients and colleagues. Harrowgate is headquartered in Chicago, with branch offices in New York, San Francisco, and London.
Since our founding in 1994, we have remained committed to:
• Building superior technology
• Capitalizing on derivatives expertise
• Developing highly-skilled professionals
• Fostering an entrepreneurial and ethical work environment
3. If you could include the outline of the skyline at the bottom, as shown on the bottom of our banner, that would be great.
On the back page I would like half of the page to include information about the software internship (information about that program is included in file 2), including the qualifications as well as the quote from the software intern. On the bottom half of the page I would like information about the trading internship (file 4), "a trader's day" and those specific qualifications. All of that information can be found in the attachments.
We are looking for a more a clean, hip, feel on the flyer. Something high tech and modern. All great ideas are welcome!
Updates
Project Deadline Extended
Reason: I now made the payment guaranteed and wanted to allow designers more time to come up with designs.
Let me know if you have any questions about the project at all.
Thank you,
Corin
Industry/Entity Type
Financial
Requirements
Should not have
- Stock photos from online sources. I would like to add either my own pictures or use the ones included below.

```html
<!DOCTYPE html>
<html lang="en">
<head>
<meta charset="utf-8">
<title>Harrowgate Recruitment Flyer</title>
<link rel="stylesheet" href="https://fonts.googleapis.com/css2?family=Mulish:ital,wght@0,400;0,600;0,700;0,800;1,400&display=swap">
<style>
:root{
  --backdrop:#585858;
  --navy:#1f3a7a;
  --navy-deep:#183066;
  --yellow:#f6c22d;
  --yellow-soft:#f9d24f;
  --slate:#7d8bb9;
  --mist:#dde2ec;
  --ink:#3a3a3a;
  --grey-text:#5a5a5a;
  --white:#ffffff;
}
*{box-sizing:border-box;margin:0;padding:0}
html,body{width:1200px;height:826px;overflow:hidden;background:var(--backdrop);font-family:"Mulish",Arial,sans-serif}
.page{position:absolute;top:53px;width:534px;height:721px;background:var(--white);overflow:hidden}
.page--front{left:54px}
.page--back{left:613px}
.abs{position:absolute}

/* front */
.front-header{left:0;top:0;width:100%;height:143px;background:var(--navy);text-align:center}
.front-header__kicker{position:absolute;top:38px;width:100%;color:var(--yellow);font-size:24px;font-weight:400}
.front-header__title{position:absolute;top:76px;width:100%;color:var(--white);font-size:36px;font-weight:600;letter-spacing:17px;padding-left:17px}
.hero-photo{left:0;top:143px;width:100%;height:341px;background:
  linear-gradient(90deg,rgba(40,50,70,.35),rgba(255,255,255,0) 40%),
  linear-gradient(180deg,#9aa6b8 0%,#c3cbd6 30%,#8791a0 55%,#5d6675 100%)}
.benefit-ring{left:134px;top:190px;width:264px;height:264px;border-radius:50%;background:rgba(255,255,255,.35)}
.benefit-disc{left:156px;top:212px;width:220px;height:220px;border-radius:50%;background:var(--yellow);display:flex;flex-direction:column;justify-content:center;align-items:center}
.benefit-disc li{list-style:none;color:var(--navy-deep);font-size:13.5px;font-weight:700;line-height:25px;text-align:center;white-space:nowrap}
.history-tab{left:60px;top:486px;width:220px;height:28px;background:var(--slate);clip-path:polygon(0 0,100% 0,94% 100%,0 100%);color:var(--white);font-size:18px;letter-spacing:1.5px;padding:2px 0 0 22px}
.history-copy{left:66px;top:527px;width:250px;color:var(--grey-text);font-size:7.9px;line-height:11.3px}
.history-copy p+p{margin-top:8px}
.history-commitments{margin-top:3px}
.history-commitments li{list-style:none;position:relative;padding-left:12px;font-weight:700;line-height:11px}
.history-commitments li::before{content:"";position:absolute;left:1px;top:3px;width:6px;height:6px;border-radius:50%;background:var(--slate)}

.brand{display:flex;align-items:center;gap:8px}
.brand__mark{width:14px;height:14px;background:var(--yellow)}
.brand__name{font-size:23px;font-weight:600;color:var(--grey-text);letter-spacing:.2px}
.brand--front{left:332px;top:560px}
.contact-icons{left:360px;top:600px;display:flex;gap:6px}
.icon{width:22px;height:22px;border-radius:50%;background:var(--yellow);display:flex;align-items:center;justify-content:center}
.address{color:var(--grey-text);font-size:11.5px;line-height:14.5px;letter-spacing:.3px}
.address--front{left:326px;top:635px}
.web{color:var(--navy);font-size:15px;font-weight:800;letter-spacing:.5px}
.web--front{left:326px;top:683px}
.foot-bar{left:316px;top:707px;width:166px;height:14px;background:var(--slate);clip-path:polygon(6% 0,94% 0,100% 100%,0 100%)}

/* back */
.building-photo{left:0;top:0;width:100%;height:155px;background:
  linear-gradient(160deg,#e9edf1 0%,#cfc6b6 35%,#a79c8a 65%,#6f6759 100%)}
.section-band{left:0;width:100%;display:flex}
.section-band h2{font-size:12.5px;font-weight:700;position:absolute;top:7px}
.band--software{top:155px;height:31px;background:var(--navy);color:var(--white)}
.band--trading{top:449px;height:29px;background:var(--yellow);color:var(--navy-deep)}
.software-panel{left:0;top:186px;width:100%;height:260px;background:var(--mist)}
.trading-panel{left:0;top:478px;width:100%;height:135px;background:var(--yellow-soft)}
.col-left{left:62px}
.col-right{left:284px}
.body-copy{width:208px;font-size:7.6px;line-height:10.8px;text-align:justify;color:var(--navy-deep)}
.body-copy p+p{margin-top:8px}
.qual-list{width:230px;font-size:7.6px;line-height:10.8px;color:var(--navy-deep)}
.qual-list li{list-style:none;position:relative;padding-left:13px}
.qual-list li::before{content:"";position:absolute;left:0;top:2px;width:6px;height:6px;background:var(--navy)}
.software-copy{top:197px}
.software-quals{top:197px}
.quote{left:53px;top:349px;width:450px;height:82px;background:var(--navy);color:var(--white);font-size:7.8px;line-height:10.8px;padding:9px 18px 0 52px}
.quote cite{display:block;color:var(--yellow);font-style:normal}
.quote-tail{left:53px;top:431px;width:0;height:0;border-top:8px solid var(--navy);border-right:10px solid transparent}
.trading-copy{top:485px;color:#2b2b2b}
.trading-quals{top:485px;color:#2b2b2b}
.trading-quals li::before{background:var(--navy)}
.brand--back{left:70px;top:650px}
.contact-stack{left:285px;top:626px;display:flex;flex-direction:column;gap:8px}
.address--back{left:323px;top:631px}
.web--back{left:323px;top:683px}
</style>
</head>
<body>

<section class="page page--front">
  <header class="abs front-header">
    <div class="front-header__kicker">Internship for</div>
    <h1 class="front-header__title">CAREER</h1>
  </header>
  <div class="abs hero-photo" role="img" aria-label="Collage of office architecture and traders at their trading desks"></div>
  <div class="abs benefit-ring"></div>
  <ul class="abs benefit-disc">
    <li>Cutting Edge Technology</li>
    <li>Excellent Pay and Benefits</li>
    <li>Free Breakfast, Lunch and Snacks</li>
    <li>Monthly Team Building Events</li>
    <li>Casual Work Attire</li>
    <li>Downtown Chicago</li>
  </ul>

  <h2 class="abs history-tab">Our History</h2>
  <div class="abs history-copy">
    <p>Harrowgate is a diversified financial institution specializing in proprietary trading, asset management, order execution services, and technology solutions. We are recognized as a market leader in derivatives valuation, trading, and value-added order execution across global equity, options, and futures markets. Our focus on innovation, achievement, and integrity serves the interests of our clients and colleagues. Harrowgate is headquartered in Chicago, with branch offices in New York, San Francisco, and London.</p>
    <p>Since our founding in 1994, we have remained committed to:</p>
    <ul class="history-commitments">
      <li>Building superior technology</li>
      <li>Capitalizing on derivatives expertise</li>
      <li>Developing highly-skilled professionals</li>
      <li>Fostering an entrepreneurial and ethical work environment</li>
    </ul>
  </div>

  <div class="abs brand brand--front"><span class="brand__mark"></span><span class="brand__name">harrowgate</span></div>
  <div class="abs contact-icons">
    <span class="icon"><svg width="12" height="12" viewBox="0 0 12 12"><path d="M6 1 1 5.5h1.5V11h2.5V8h2v3h2.5V5.5H11z" fill="#fff"/></svg></span>
    <span class="icon"><svg width="12" height="12" viewBox="0 0 12 12"><path d="M3 1h2l1 3-1.3 1a6 6 0 0 0 2.3 2.3L8 6l3 1v2c0 1-1 2-2 2A8 8 0 0 1 1 3c0-1 1-2 2-2z" fill="#fff"/></svg></span>
    <span class="icon"><svg width="12" height="12" viewBox="0 0 12 12"><rect x="1" y="3" width="10" height="7" fill="#fff"/><path d="M1 3l5 4 5-4" stroke="#f6c22d" stroke-width="1" fill="none"/></svg></span>
  </div>
  <address class="abs address address--front">480 W. Marlow Street, 2nd Floor<br>Chicago, IL &nbsp;60607<br>Phone: (312) 555-0148</address>
  <div class="abs web web--front">www.harrowgate-co.com</div>
  <div class="abs foot-bar"></div>
</section>

<section class="page page--back">
  <div class="abs building-photo" role="img" aria-label="Upward view of a tall stone office building facade with rows of windows"></div>

  <div class="abs section-band band--software">
    <h2 class="col-left">Software Engineer Internship</h2>
    <h2 style="left:288px">Qualifications</h2>
  </div>
  <div class="abs software-panel"></div>
  <div class="abs body-copy col-left software-copy">
    <p>Harrowgate Trading's internship program for Software Engineers offers qualified candidates a unique opportunity to experience the full development lifecycle, while building custom trading applications for a leader in the industry. You will work with a team of top technology professionals, and interact with senior partners and traders, to design and maintain software.</p>
    <p>Our 12 week summer internship program serves as a source of hiring full time software engineers. All employees and interns have access to our full-time education department and Director of Education. We are constantly creating new curriculum that informs and leads to collaborative innovation at the firm.</p>
  </div>
  <ul class="abs qual-list col-right software-quals">
    <li>Bachelor's or Master's degree in Computer Science or Computer Engineering (or pursuing one of these degrees for our internship – must have Junior standing or be in your first year of a two-year Master's program)</li>
    <li>History of academic excellence, with a minimum 3.0 GPA</li>
    <li>Solid understanding of object-oriented design and development</li>
    <li>Knowledge of C++, C#, the .NET framework, and SQL is preferred, but not required</li>
    <li>Excellent problem solving skills</li>
    <li>Desire to work in a team environment</li>
    <li>Interest in financial markets</li>
  </ul>
  <blockquote class="abs quote">"The best part of my internship is coming into the office, sitting down, and getting to work developing real software for a real company with a team that has gone so far out of their way to help me learn and improve. In fact, I almost never felt like an intern. I felt completely welcomed by my team. They have treated me like a full-time employee 100% of the time. It felt great to be useful and make a real contribution to the team."<cite>-Software Intern '13</cite></blockquote>
  <div class="abs quote-tail"></div>

  <div class="abs section-band band--trading">
    <h2 class="col-left">A Trader's Day</h2>
    <h2 style="left:286px">Qualifications</h2>
  </div>
  <div class="abs trading-panel"></div>
  <div class="abs body-copy col-left trading-copy">
    <p>The typical day for a trader involves staying current on the markets and quickly reacting to changing and unexpected market conditions. Our traders are constantly innovating to improve our existing trading logic and to develop new trading algorithms. Collaboration and the development of unique strategies, in addition to the review and analysis of the markets and our own trading results, is an everyday occurrence as we strive for improvement.</p>
  </div>
  <ul class="abs qual-list col-right trading-quals">
    <li>Working toward a degree in engineering, computer science, finance, economics or mathematics</li>
    <li>Junior or graduate standing</li>
    <li>History of academic excellence</li>
    <li>Demonstrated interest in trading, financial markets, and technology</li>
    <li>Excellent quantitative and problem solving skills</li>
    <li>Entrepreneurial and self-motivated</li>
    <li>Strong communication skills and a desire to work in a team environment</li>
    <li>3-month commitment</li>
    <li>Basic knowledge of C++, C#, the .NET framework,</li>
  </ul>

  <div class="abs brand brand--back"><span class="brand__mark"></span><span class="brand__name">harrowgate</span></div>
  <div class="abs contact-stack">
    <span class="icon"><svg width="12" height="12" viewBox="0 0 12 12"><path d="M6 1 1 5.5h1.5V11h2.5V8h2v3h2.5V5.5H11z" fill="#fff"/></svg></span>
    <span class="icon"><svg width="12" height="12" viewBox="0 0 12 12"><path d="M3 1h2l1 3-1.3 1a6 6 0 0 0 2.3 2.3L8 6l3 1v2c0 1-1 2-2 2A8 8 0 0 1 1 3c0-1 1-2 2-2z" fill="#fff"/></svg></span>
    <span class="icon"><svg width="12" height="12" viewBox="0 0 12 12"><rect x="1" y="3" width="10" height="7" fill="#fff"/><path d="M1 3l5 4 5-4" stroke="#f6c22d" stroke-width="1" fill="none"/></svg></span>
  </div>
  <address class="abs address address--back">480 W. Marlow Street, 2nd Floor<br>Chicago, IL &nbsp;60607<br>Phone: (312) 555-0148</address>
  <div class="abs web web--back">www.harrowgate-co.com</div>
</section>

</body>
</html>
```